Financial Broker firm looking for Brochure design/Pdf-document

Job Type
Brochure Design/PDF-Document
Task Outline
Create a Brochure Design that also works for sending as pdf-document.
Task Description
We need a combined corporate brochure (Booklet style) to give out to potential clients as well as sending it to potential clients through Internet as pdf-document.
We need a background template with pictures and colors that gives the impression of professionalism, trustworthiness and seriousness. Attached text in English but the text will be translated into different languages to fit different markets. Therefore we would like to receive one template including the text and one without any text (but with the logo). Please inform us where (any) pictures and/or photos on the template have been taken from in order for us to buy and use them legally.
About Us
Our company Kelvora Trust AB is a financial brokerage company who provides a diversity of services for different selected partners (www.kelvoratrust.example).
Target Market
Companies on all levels, domestic or international
Requirements
Must Have:
-The text and logo attached below
Industry/Entity Type
Financial
Look and feel

```html
<!DOCTYPE html>
<html lang="en">
<head>
<meta charset="utf-8">
<title>Kelvora Trust AB – Brochure Spread</title>
<link href="https://fonts.googleapis.com/css2?family=Roboto:wght@300;400;700&display=swap" rel="stylesheet">
<style>
  :root {
    --page: #ffffff;
    --ink: #1a1a1a;
    --black: #000000;
    --navy: #0b1e38;
    --cyan: #19e3f0;
    --panel-grey: #c9c9c9;
    --shadow: rgba(0,0,0,0.28);
  }
  html, body {
    margin: 0;
    padding: 0;
    width: 1200px;
    height: 1000px;
    overflow: hidden;
    background: var(--page);
  }
  .canvas {
    position: relative;
    width: 1200px;
    height: 1000px;
    font-family: "Roboto", Arial, sans-serif;
    color: var(--ink);
  }
  .spread {
    position: absolute;
    left: 134px;
    top: 152px;
    width: 936px;
    height: 701px;
    background: var(--page);
    box-shadow: 0 4px 18px var(--shadow);
    overflow: hidden;
  }
  .page { position: absolute; top: 0; height: 701px; }
  .page--left { left: 0; width: 467px; }
  .page--right { left: 467px; width: 469px; border-left: 1px solid #d6d6d6; box-sizing: border-box; }

  .top-band {
    position: absolute; left: 0; top: 0; width: 467px; height: 119px;
    background: var(--black);
  }
  .section-title {
    position: absolute;
    top: 60px;
    height: 59px;
    background: var(--navy);
    color: var(--cyan);
    font-size: 22px;
    font-weight: 300;
    line-height: 59px;
    margin: 0;
    white-space: nowrap;
  }
  .section-title strong { font-weight: 700; }
  .page--left .section-title { left: 63px; width: 404px; padding-left: 13px; box-sizing: border-box; }
  .page--right .section-title { left: 0; width: 405px; text-align: center; }

  .illustration {
    position: absolute;
    left: 86px; top: 178px; width: 330px; height: 210px;
    background: radial-gradient(ellipse at 45% 55%, #e4f4ee 0%, #cfe9e0 45%, #ffffff 80%);
  }
  .body-copy {
    position: absolute;
    margin: 0;
    font-weight: 300;
    text-align: justify;
  }
  .page--left .body-copy {
    left: 63px; top: 393px; width: 363px;
    font-size: 13.6px; line-height: 21.6px;
  }

  .info-panel {
    position: absolute; left: 0; top: 125px; width: 469px; height: 346px;
    background: var(--panel-grey);
  }
  .info-panel .body-copy {
    left: 44px; width: 354px;
    font-size: 13.2px; line-height: 19.8px;
  }
  .info-panel .body-copy.first { top: 11px; }
  .info-panel .body-copy.second { top: 230px; }

  .photo {
    position: absolute; left: 0; top: 471px; width: 397px; height: 230px;
    background: linear-gradient(135deg, #e8ecee 0%, #b9c7d4 45%, #8aa1b8 70%, #d8dde0 100%);
  }
  .photo-edge {
    position: absolute; left: 397px; top: 471px; width: 72px; height: 230px;
    background: var(--black);
  }
</style>
</head>
<body>
<div class="canvas">
  <div class="spread">
    <section class="page page--left">
      <div class="top-band"></div>
      <h2 class="section-title"><strong>Covering</strong> financial risks</h2>
      <div class="illustration" role="img" aria-label="3D illustration of a golden dollar sign balanced on a seesaw between a rising red arrow and a falling green arrow"></div>
      <p class="body-copy">With international payments you most likely have paid or received different amounts from foreign currencies. This is called fluctuations in the currency market. The service we provide will help you to identify risks and how you can cover them.We are working with different partners that will cover your currency risks.They can also assist you with avoiding commodity risks for your production,for example protecting the price of a production commodity or interest rate risks, if you have a variable loan. The burden of a rise in the interest rate may be expensiveto your company.If you are interested, there is also the option by remunerate your liquidity through our partners' cash certificate deposit.</p>
    </section>

    <section class="page page--right">
      <h2 class="section-title"><strong>Trade Credit</strong> Insurance</h2>
      <div class="info-panel">
        <p class="body-copy first">With a Trade Credit Insurance, you do not need to worry about your customers not being able to pay your bills or have to set aside funds for bad debts. Instead trade credit insurance provides a vital injection against non-payment of goods or services, both in the domestic as well as your export market.&nbsp; We know that many unpaid invoices are caused by insufficient knowledge about your customers' solvency. In the event of insolvency or payment default, credit insurance gives you swift access to replacement capital without harming your balance sheet.</p>
        <p class="body-copy second">The insurance is also applicable on attracting new clients, which gives your company the possibility to increase sales, open new markets and increase profits. Having a trade credit insurance is responsible business management, as it protects the cash flow and net profit of your company.</p>
      </div>
      <div class="photo" role="img" aria-label="Photo of two businessmen shaking hands across a glass table in a bright office while a woman looks on"></div>
      <div class="photo-edge"></div>
    </section>
  </div>
</div>
</body>
</html>
```